Stylish Business Card for Modern hair salon

I need a simple business card design using our salon logo and colours that are in the logo. We service clients of all ages but predominantly those in the 18 to 55 age range. We have a young staff and are looking to have a card that will present a modern and clean image that represents who we are. The card should be in black and white same as our logo. Minimal use of other colours is allowed.

Industry/Entity Type

Hair And Beauty

Contact Information for Business Card

The design should have the following information
salon name - TZ Hair Studio
address - 2957 Fernbrook Rd.W. Brookvale, ON L8R3P2
phone - 555 641-2087
website - tzhairexample.ca
instagram - tz.hairstudio
twitter - @TZ_HairStudio

Colors
000000
ffffff
474747

Requirements
Must have
• simple design, salon name, address, phone, website, instagram, twitter info
• Back of card should have the following:
• YOUR NEXT APPOINTMENT
• DATE
• TIME
Nice to have
• simple design, clear to see and read,
• predominantly black and white colour, minimal use of other colours is ok
Should not have
• many colours, various fonts

```html
<!DOCTYPE html>
<html lang="en">
<head>
<meta charset="utf-8">
<title>TZ Hair Studio – Business Card</title>
<link rel="stylesheet" href="https://fonts.googleapis.com/css2?family=Playfair+Display:wght@400;500&family=Roboto:wght@400&display=swap">
<style>
  :root {
    --black: #000000;
    --card: #111111;
    --white: #ffffff;
    --grey: #474747;
    --band: #d9d9d9;
    --backdrop: #e6e4e1;
    --soft: #bdbdbd;
  }
  * { margin: 0; padding: 0; box-sizing: border-box; }
  html, body { width: 1200px; height: 715px; overflow: hidden; }
  body {
    background: var(--backdrop);
    font-family: "Roboto", Arial, sans-serif;
    display: flex;
    align-items: center;
    justify-content: center;
    gap: 40px;
  }
  .card {
    position: relative;
    width: 540px;
    height: 309px;
    background: var(--card);
    color: var(--white);
    box-shadow: 0 6px 18px rgba(0,0,0,.25);
    overflow: hidden;
  }

  /* Back: appointment card */
  .back-name {
    position: absolute;
    left: 0; right: 0;
    top: 88px;
    text-align: center;
    font-family: "Playfair Display", Georgia, serif;
    font-weight: 400;
    font-size: 34px;
    line-height: 1;
    color: var(--grey);
  }
  .appointment-title {
    position: absolute;
    right: 40px;
    top: 178px;
    font-size: 12px;
    letter-spacing: 2px;
    color: var(--soft);
  }
  .appointment-band {
    position: absolute;
    left: 0; right: 0;
    bottom: 40px;
    height: 58px;
    background: var(--band);
    color: var(--black);
    display: flex;
    align-items: flex-end;
    gap: 24px;
    padding: 0 28px 16px;
    font-size: 11px;
    letter-spacing: 1.5px;
  }
  .field { display: flex; align-items: flex-end; gap: 8px; flex: 1; }
  .field-line { flex: 1; border-bottom: 1px solid var(--black); height: 1px; margin-bottom: 3px; }

  /* Front: contact card */
  .studio-name {
    position: absolute;
    left: 30px;
    top: 28px;
    font-family: "Playfair Display", Georgia, serif;
    font-weight: 500;
    font-size: 19px;
  }
  .contact-list {
    position: absolute;
    left: 30px;
    bottom: 34px;
    list-style: none;
    font-size: 12.5px;
    line-height: 18px;
  }
  .contact-list li { display: flex; align-items: flex-start; gap: 8px; }
  .contact-list svg { width: 11px; height: 11px; margin-top: 3px; flex: none; }
  .contact-list .indent { padding-left: 19px; }
  .social-list {
    position: absolute;
    right: 34px;
    top: 112px;
    list-style: none;
    font-size: 12.5px;
    line-height: 19px;
  }
  .social-list li { display: flex; align-items: center; gap: 8px; }
  .social-dot { width: 10px; height: 10px; border-radius: 50%; background: var(--white); }
  .front-name {
    position: absolute;
    right: 34px;
    bottom: 40px;
    font-family: "Playfair Display", Georgia, serif;
    font-weight: 400;
    font-size: 30px;
    line-height: 1;
    color: var(--white);
  }
</style>
</head>
<body>
  <section class="card card-back" aria-label="Card back: appointment reminder">
    <div class="back-name">TZ Hair Studio</div>
    <p class="appointment-title">YOUR NEXT APPOINTMENT</p>
    <div class="appointment-band">
      <div class="field"><span>DATE</span><span class="field-line"></span></div>
      <div class="field"><span>TIME</span><span class="field-line"></span></div>
    </div>
  </section>

  <section class="card card-front" aria-label="Card front: contact details">
    <h1 class="studio-name">TZ Hair Studio</h1>

    <ul class="social-list">
      <li><span class="social-dot"></span>tz.hairstudio</li>
      <li><span class="social-dot"></span>@TZ_HairStudio</li>
    </ul>

    <ul class="contact-list">
      <li>
        <svg viewBox="0 0 12 12" aria-hidden="true"><path d="M1 3c0-1 1-2 2-2l1.5 2.5-1 1c.7 1.5 1.8 2.6 3 3l1-1L10 8c0 1-1 2-2 2C4 10 1 7 1 3z" fill="#fff"/></svg>
        <span>555 641-2087</span>
      </li>
      <li>
        <svg viewBox="0 0 12 12" aria-hidden="true"><circle cx="6" cy="6" r="5" fill="none" stroke="#fff" stroke-width="1.2"/><path d="M1 6h10M6 1c-2.5 3-2.5 7 0 10M6 1c2.5 3 2.5 7 0 10" fill="none" stroke="#fff" stroke-width="1"/></svg>
        <span>www.tzhairexample.ca</span>
      </li>
      <li>
        <svg viewBox="0 0 12 12" aria-hidden="true"><path d="M6 11S2 7 2 4.5a4 4 0 0 1 8 0C10 7 6 11 6 11z" fill="none" stroke="#fff" stroke-width="1.2"/><circle cx="6" cy="4.5" r="1.4" fill="#fff"/></svg>
        <span>2957 Fernbrook Rd.W.</span>
      </li>
      <li class="indent">Brookvale, ON L8R3P2</li>
    </ul>

    <div class="front-name">TZ Hair Studio</div>
  </section>
</body>
</html>
```